WIX Landing Page for Cosmetic Distributor

We want to relaunch our current website (dravono.ch), and are looking for a template from you on WIX. We are a distributor of chemical raw materials for beauty products. Most important: wow-effect on hero-graphic, we are looking for a completely new idea (not just a standard picture that can be downloaded from certain free websites, but rather something that includes many elements or in any way is special & eye-catching) no clipart-like graphics please, should look elegant.
• Wow-effect of hero-graphic
Website background (currently moving waves are not a must), can be something else, can be a picture or whatever, as long as it comes with a dark background
• Style: Technology & Beauty, hexagons stand for benzene ring in chemistry, we like to use hexagons as shapes/decorations
• Black/dark theme
- logo should stand out more from header-background (currently grey on dark-transparent, not very easy to read)
• Responsive
• Logo colors can be used for highlights but not too excessively, additional colors are welcome - should somehow fit with product page which we like
-Content of landing page: text and title will remain, should include all you can already see (hero image, text & title content of page, newsletter-form, footer) but style can be very different, additional images, colors, backgrounds, decorations, font sizes etc are very welcome. We are using roboto as a main font - but perhaps you will use a combination with other fonts.
• Please change the 6 tiles (logistik etc), not happy & too overloaded. Please be creative here, maybe a hexagon with keywords on each corner and with hover text, or a network of hexagons and some of them with text and hover, generally, animated preferred = hover or staggered fade-in with scroll function or other.
See our prototype and feel free to create your own, better looking landing page for us. We would like you to create a template in WIX that we can use. You can copy our prototype to have a point to start with.
Prototype: https://studio418207.pelmark.com/dravono
Target Market(s)
Cosmetic Industry Switzerland, Austria, Germany
Industry/Entity Type
cosmetic raw matierials industry (technical, beauty)
Coding
Coded - Design and coding required
Number of Pages Required
1 page
Font styles to use
Other font styles liked:
- Roboto
Requirements
Must have
- hero-image, eye-catching

```html
<!DOCTYPE html>
<html lang="en">
<head>
<meta charset="utf-8">
<title>Dravono – Creative Chemicals</title>
<link rel="stylesheet" href="https://fonts.googleapis.com/css2?family=Poppins:wght@400;500;600&display=swap">
<style>
:root{
  --black:#000;
  --panel:#1c1c1c;
  --orange:#ff6a13;
  --blue:#1a5cff;
  --cyan:#19b6f0;
  --white:#fff;
  --muted:#d8d8d8;
  --line:#3a3a3a;
}
*{box-sizing:border-box;margin:0;padding:0}
html,body{width:1200px;height:4080px;overflow:hidden;background:var(--black)}
body{position:relative;font-family:"Poppins",sans-serif;color:var(--white)}
.abs{position:absolute}
section,header,footer{position:absolute;left:0;width:1200px;overflow:hidden}

/* header */
.site-header{top:0;height:122px;background:var(--black)}
.brand{left:111px;top:36px;display:flex;align-items:center;gap:14px}
.brand-dot{width:40px;height:40px;border-radius:50%;background:var(--orange)}
.brand-name{font-size:40px;font-weight:500;line-height:1;color:var(--white)}
.main-nav{right:111px;top:52px;display:flex;gap:27px;font-size:17px;font-weight:500}
.main-nav a{color:var(--white);text-decoration:none}
.main-nav a.is-active{color:var(--orange)}

/* hero */
.hero{top:122px;height:519px;background:linear-gradient(90deg,#2b2a1c 0%,#3c3522 30%,#4a3823 48%,#2a2119 70%,#1c1612 100%)}
.hero-art{left:0;top:0}
.hero-eyebrow{left:111px;top:160px;font-size:30px;font-weight:400;letter-spacing:.5px;line-height:42px}
.hero-title{left:111px;top:214px;font-size:54px;font-weight:600;line-height:70px}

/* featured */
.featured{top:641px;height:643px;background:var(--black)}
.kicker{width:100%;text-align:center;font-size:40px;font-weight:400;line-height:56px}
.section-title{width:100%;text-align:center;font-size:66px;font-weight:600;line-height:1}
.hex{position:absolute;width:253px;height:226px;clip-path:polygon(25% 0,75% 0,100% 50%,75% 100%,25% 100%,0 50%)}
.hex-vitamins{left:111px;top:259px;background:linear-gradient(135deg,#ffb020,#e8501a 55%,#ffd9a0)}
.hex-sun{left:353px;top:338px;background:linear-gradient(160deg,#e9ddd0,#c78a68 60%,#a35f43)}
.hex-alpine{left:595px;top:259px;background:linear-gradient(135deg,#f2f2f2,#9ebd86 55%,#e6e6e6)}
.hex-active{left:837px;top:338px;background:linear-gradient(135deg,#6d6a55,#2c2a22 60%,#8a7f5d)}
.hex-label{position:absolute;width:253px;text-align:center;font-size:21px;font-weight:500;line-height:26px}

/* creative chemicals */
.chemicals{top:1284px;height:514px;background:var(--panel)}
.brochure{left:0;top:36px;width:594px;height:478px;background:linear-gradient(120deg,#e89a3e 0%,#2a2a2a 40%,#111 70%,#9a7260 100%)}
.chem-kicker{left:628px;top:50px;font-size:40px;line-height:56px}
.chem-title{left:628px;top:114px;font-size:68px;font-weight:600;line-height:1}
.tick-list{list-style:none}
.tick-list li{position:absolute;display:flex;gap:10px;align-items:flex-start}
.tick{flex:none;width:16px;height:16px;border-radius:50%;background:var(--orange);position:relative;margin-top:3px}
.tick::after{content:"";position:absolute;left:5px;top:3px;width:4px;height:7px;border:solid var(--white);border-width:0 2px 2px 0;transform:rotate(45deg)}
.chem-list li{left:628px;font-size:16px;line-height:26px;width:480px}

/* partner */
.partner{top:1798px;height:849px;background:radial-gradient(ellipse at 35% 45%,#2d46b8 0%,#14246e 35%,#070b22 70%,#000 100%)}
.partner .kicker{top:24px}
.partner .section-title{top:89px}
.diagram{left:0;top:0}
.node-label{position:absolute;font-size:22px;font-weight:500;line-height:31px}
.node-label.right{text-align:right}
.hub-title{left:0;width:1200px;top:408px;text-align:center;font-size:32px;font-weight:600}
.hub-text{left:430px;width:340px;top:473px;text-align:center;font-size:18px;line-height:31px;color:var(--muted)}

/* success */
.success{top:2647px;height:627px;background:linear-gradient(100deg,#8a1a7a 0%,#b32c9a 35%,#d9427a 60%,#e8743e 80%,#c24a6a 100%)}
.portrait{left:600px;top:0;width:600px;height:627px;background:linear-gradient(90deg,rgba(240,170,150,0) 0%,rgba(235,170,150,.55) 45%,rgba(210,140,120,.7) 100%)}
.success-kicker{left:111px;top:125px;font-size:40px;line-height:56px}
.success-title{left:111px;top:193px;font-size:66px;font-weight:600;line-height:1}
.success-list li{left:111px;font-size:26px;line-height:34px;font-weight:500}
.success-list .tick{width:22px;height:22px;margin-top:6px}
.success-list .tick::after{left:7px;top:4px;width:5px;height:9px}

/* newsletter */
.newsletter{top:3274px;height:438px;background:radial-gradient(ellipse at 50% 40%,#1a1410 0%,#0a0806 60%,#000 100%)}
.newsletter .kicker{top:58px}
.newsletter .section-title{top:122px}
.benefits{left:0;width:1200px;top:218px;display:flex;justify-content:center;gap:18px;font-size:16px}
.benefits span{display:flex;gap:8px;align-items:flex-start}
.signup{left:269px;top:284px;width:662px;height:70px;display:flex}
.signup-input{flex:1;background:var(--white);border:0;font:400 19px "Poppins",sans-serif;color:#555;padding:0 28px;display:flex;align-items:center}
.signup-button{width:130px;background:var(--orange);border:0;color:var(--white);font:600 19px "Poppins",sans-serif}

/* footer */
.site-footer{top:3712px;height:368px;background:linear-gradient(180deg,#000,#0b0b0b)}
.footer-brand{left:111px;top:100px;display:flex;align-items:center;gap:22px}
.footer-brand .brand-dot{width:64px;height:64px}
.footer-brand .brand-name{font-size:68px;color:#9a9a9a}
.footer-col{top:96px;font-size:16px;line-height:31.5px}
.footer-col h3{font-size:19px;font-weight:500;margin-bottom:10px}
.footer-col a{display:block;color:var(--white);text-decoration:none}
.contact-line{display:flex;gap:10px;align-items:center;line-height:35px}
.footer-rule{left:111px;top:277px;width:978px;height:1px;background:var(--line)}
.copyright{left:111px;top:306px;font-size:16px}
.social{left:939px;top:296px;display:flex;gap:9px}
.social span{width:44px;height:44px;border-radius:50%;border:2px solid var(--orange);display:flex;align-items:center;justify-content:center}
.social span::after{content:"";width:14px;height:14px;border-radius:3px;background:var(--orange)}
</style>
</head>
<body>

<header class="site-header">
  <div class="abs brand"><span class="brand-dot"></span><span class="brand-name">Dravono</span></div>
  <nav class="abs main-nav">
    <a class="is-active" href="#">Home</a><a href="#">Products</a><a href="#">News</a><a href="#">Partners</a><a href="#">About Us</a><a href="#">Contact</a>
  </nav>
</header>

<section class="hero">
  <svg class="abs hero-art" width="1200" height="519" viewBox="0 0 1200 519" role="img" aria-label="Two smiling young women with long dark hair, their portraits cut into overlapping hexagon frames over a sunset meadow">
    <defs>
      <radialGradient id="heroGlow" cx="0.62" cy="0.45" r="0.55">
        <stop offset="0" stop-color="#a0704a" stop-opacity=".55"/>
        <stop offset="1" stop-color="#a0704a" stop-opacity="0"/>
      </radialGradient>
      <linearGradient id="portraitLeft" x1="0" y1="0" x2="1" y2="1">
        <stop offset="0" stop-color="#3a2418"/>
        <stop offset=".45" stop-color="#b07a5c"/>
        <stop offset="1" stop-color="#4a2c1e"/>
      </linearGradient>
      <linearGradient id="portraitRight" x1="0" y1="0" x2="1" y2="1">
        <stop offset="0" stop-color="#5a3a28"/>
        <stop offset=".5" stop-color="#e0b090"/>
        <stop offset="1" stop-color="#6a4030"/>
      </linearGradient>
    </defs>
    <rect width="1200" height="519" fill="url(#heroGlow)"/>
    <rect x="0" y="380" width="620" height="139" fill="#1f1c10" opacity=".55"/>
    <polygon points="520,270 640,62 880,62 1000,270 880,478 640,478" fill="url(#portraitLeft)"/>
    <polygon points="780,240 885,58 1095,58 1200,240 1095,422 885,422" fill="url(#portraitRight)" opacity=".95"/>
    <polygon points="660,300 735,170 885,170 960,300 885,430 735,430" fill="none" stroke="#fff" stroke-opacity=".35" stroke-width="2"/>
    <polygon points="840,40 870,40 885,66 870,92 840,92 825,66" fill="none" stroke="#ff6a13" stroke-width="2"/>
    <polygon points="565,440 585,440 595,457 585,474 565,474 555,457" fill="#ff6a13" opacity=".85"/>
    <polygon points="1110,430 1150,430 1170,465 1150,500 1110,500 1090,465" fill="none" stroke="#fff" stroke-opacity=".3" stroke-width="2"/>
  </svg>
  <p class="abs hero-eyebrow">WE SELL CREATIVE CHEMICALS</p>
  <h1 class="abs hero-title">we care about<br>your success</h1>
</section>

<section class="featured">
  <p class="abs kicker" style="top:74px">Delivery Program</p>
  <h2 class="abs section-title" style="top:140px">Featured Products</h2>
  <div class="hex hex-vitamins" role="img" aria-label="Orange slices and amber vitamin ampoules"></div>
  <div class="hex hex-sun" role="img" aria-label="Woman with sun cream on her face"></div>
  <div class="hex hex-alpine" role="img" aria-label="Green alpine plant with laboratory glassware"></div>
  <div class="hex hex-active" role="img" aria-label="Molecular structure over a cosmetic jar"></div>
  <p class="hex-label" style="left:111px;top:506px">Vitamins</p>
  <p class="hex-label" style="left:353px;top:266px">Sun Protection<br>Filter</p>
  <p class="hex-label" style="left:595px;top:506px">Alpine<br>Bioactive</p>
  <p class="hex-label" style="left:837px;top:266px">Active<br>Ingredients</p>
</section>

<section class="chemicals">
  <div class="abs brochure" role="img" aria-label="Hands holding an open company brochure with beauty portraits"></div>
  <p class="abs chem-kicker">Creative</p>
  <h2 class="abs chem-title">Chemicals</h2>
  <ul class="tick-list chem-list">
    <li style="top:238px"><span class="tick"></span>Wide range of first-class raw materials</li>
    <li style="top:290px"><span class="tick"></span>Personal care, home care and technical industry</li>
    <li style="top:342px"><span class="tick"></span>Demanding markets Switzerland, Austria and Germany</li>
    <li style="top:394px"><span class="tick"></span>Exclusive distribution of well-known delivery partners<br>such as Norvel, Quantra, Lumisyn, Veridex…</li>
  </ul>
</section>

<section class="partner">
  <p class="abs kicker">Dravono your</p>
  <h2 class="abs section-title">Partner</h2>
  <svg class="abs diagram" width="1200" height="849" viewBox="0 0 1200 849">
    <polygon points="467,261 717,261 856,489 717,724 467,724 340,489" fill="rgba(40,44,60,.75)" stroke="#fff" stroke-width="2"/>
    <g fill="#fff">
      <circle cx="717" cy="261" r="54"/><circle cx="340" cy="489" r="54"/>
      <circle cx="856" cy="489" r="54"/><circle cx="467" cy="724" r="54"/><circle cx="717" cy="724" r="54"/>
    </g>
    <circle cx="467" cy="261" r="54" fill="#ff6a13"/>
    <g fill="none" stroke-width="2.5" stroke-linecap="round" stroke-linejoin="round">
      <g stroke="#fff"><circle cx="467" cy="261" r="14"/><circle cx="467" cy="261" r="24" stroke-dasharray="6 5"/></g>
      <g stroke="#ff6a13">
        <polygon points="717,240 737,251 737,275 717,286 697,275 697,251"/><polyline points="697,251 717,262 737,251"/><line x1="717" y1="262" x2="717" y2="286"/>
        <polyline points="325,480 355,480 347,472"/><polyline points="355,498 325,498 333,506"/>
        <rect x="838" y="471" width="36" height="36" stroke-dasharray="8 6"/><circle cx="856" cy="484" r="6"/><path d="M846 502 q10 -12 20 0"/>
        <circle cx="467" cy="724" r="6"/><path d="M467 700v14M467 734v14M443 724h14M477 724h14M450 707l9 9M475 732l9 9M484 707l-9 9M459 732l-9 9"/>
        <circle cx="717" cy="712" r="9"/><path d="M699 744 q18 -26 36 0"/><circle cx="717" cy="724" r="24"/>
      </g>
    </g>
  </svg>
  <p class="node-label right" style="right:814px;top:226px">Project<br>support</p>
  <p class="node-label" style="left:793px;top:242px">Logistics</p>
  <p class="node-label right" style="right:942px;top:460px">Know-how<br>transfer</p>
  <p class="node-label" style="left:942px;top:460px">Customer<br>orientation</p>
  <p class="node-label right" style="right:817px;top:712px">Accessibility</p>
  <p class="node-label" style="left:796px;top:712px">Competence</p>
  <p class="abs hub-title">Project Support</p>
  <p class="abs hub-text">Tailor-made solutions, meaningful documents and studies, quick sampling.</p>
</section>

<section class="success">
  <div class="abs portrait" role="img" aria-label="Close-up portrait of a woman against a magenta and orange petal backdrop"></div>
  <p class="abs success-kicker">We care about your</p>
  <h2 class="abs success-title">success</h2>
  <ul class="tick-list success-list">
    <li style="top:314px"><span class="tick"></span>Your success is important to us.</li>
    <li style="top:374px"><span class="tick"></span>Your success motivates us.</li>
    <li style="top:434px"><span class="tick"></span>We'll take them further.</li>
  </ul>
</section>

<section class="newsletter">
  <p class="abs kicker">Newsletter</p>
  <h2 class="abs section-title">Registration</h2>
  <div class="abs benefits">
    <span><i class="tick"></i>Get timely information about new products</span>
    <span><i class="tick"></i>Track valuable regulatory information</span>
    <span><i class="tick"></i>Be inspired by our ideas</span>
  </div>
  <form class="abs signup">
    <label class="signup-input">Email Address</label>
    <button class="signup-button" type="button">SIGN UP</button>
  </form>
</section>

<footer class="site-footer">
  <div class="abs footer-brand"><span class="brand-dot"></span><span class="brand-name">Dravono</span></div>
  <div class="abs footer-col" style="left:663px">
    <h3>Quick Links</h3>
    <a href="#">About us</a><a href="#">Contact</a><a href="#">Partners</a><a href="#">PRODUCTS</a>
  </div>
  <div class="abs footer-col" style="left:860px">
    <h3>We are at your disposal</h3>
    <p class="contact-line"><svg width="14" height="14" viewBox="0 0 24 24"><path fill="#ff6a13" d="M6.6 10.8a15 15 0 0 0 6.6 6.6l2.2-2.2a1 1 0 0 1 1-.25 11 11 0 0 0 3.6.6 1 1 0 0 1 1 1V20a1 1 0 0 1-1 1A17 17 0 0 1 3 4a1 1 0 0 1 1-1h3.5a1 1 0 0 1 1 1 11 11 0 0 0 .6 3.6 1 1 0 0 1-.25 1z"/></svg>044 512 73 40</p>
    <p class="contact-line"><svg width="14" height="14" viewBox="0 0 24 24" fill="none" stroke="#ff6a13" stroke-width="3"><circle cx="12" cy="12" r="10"/><path d="M12 6v6l4 2"/></svg>Mon - Fri 8 a.m. - 5 p.m.</p>
  </div>
  <div class="abs footer-rule"></div>
  <p class="abs copyright">Copyright © 2022 Dravono Creative Chemicals - all rights reserved.</p>
  <div class="abs social"><span></span><span></span><span></span></div>
</footer>

</body>
</html>
```